KLD Photography Editing & Support Services for Real Estate

We require a double sided A4 flyer to promote our photography services to real estate agencies.
This particular service is targeted to rural areas where reliable, professional and highly skilled photographers are difficult to source. We teach the agent how to photograph, they upload files to a server and we take care of the rest (image editing, quality control and delivery). This will give the agents flexibility with when to shoot and eliminates the stress of managing a photographer / contractor. We offer a 1 day face to face training session and competitive packages for equipment start up.
We would like the flyer to look clean & very professional. The flyer should showcase samples of our work to highlight what can be achieved by using our services. We like the look of a black or dark background behind the text and feel that would look nice with our photographs provided. Otherwise open to your suggestions and ideas.
TEXT FOR FLYER:
Welcome to the KLD Real Estate Photography Editing and Support Service
• Take your real estate business to the next level by providing impressive real estate imagery that makes you stands out from the competition
• Omit the stress of trying to find a good photographer or managing an unreliable one and hence have more time to focus on other aspects of your business
• Showcase your listings with better quality and more impactful photographs than your competitors thereby increasing potential for a quick sale
• Great first impressions matter and you will achieve this by looking and feeling more professional. This will attract and retain more future clients.
HOW IT WORKS
• We understand that your time is valuable, so let us handle the editing and delivery of your images. You shoot, and we take care of the rest.
• Images are edited and delivered within 1 working day
INCLUSIONS:
• Full day face to face training (we come to you) and instructional handbook
• We will teach you everything you need to know about your equipment and how to take stunning real estate photographs
• Service turnaround within 1 working day
• Free HELP desk service Mon-Fri
• 12 month Exclusivity (rural towns only) for a limited time
INVESTMENT
• 99 per listing for us to manage images including editing, quality control and delivery (10 Images)
• Ask us about competitive packages for photography equipment if required
SUMMARY
The KLD Real Estate Photography Editing and Support Service is the perfect solution for busy real estate professionals who want to take their business to the next level. Our service is affordable, flexible, and designed to help you showcase your listings in the best possible light.
Contact us today to learn more about how we can help you.

```html
<!DOCTYPE html>
<html lang="en">
<head>
<meta charset="utf-8">
<title>KLD Real Estate Photography Flyer</title>
<link href="https://fonts.googleapis.com/css2?family=Cinzel:wght@400;700&family=Montserrat:wght@400&display=swap" rel="stylesheet">
<style>
  :root {
    --backdrop: #48484a;
    --page: #000000;
    --gold: #b8952a;
    --gold-light: #c9a73a;
    --white: #ffffff;
    --grey-text: #8c8c8c;
    --summary-bg: #e6e6e6;
    --summary-text: #222222;
  }
  * { margin: 0; padding: 0; box-sizing: border-box; }
  html, body { width: 1200px; height: 887px; overflow: hidden; background: var(--backdrop); }
  body { position: relative; font-family: "Montserrat", Arial, sans-serif; color: var(--white); }

  .page {
    position: absolute; top: 130px; width: 486px; height: 628px;
    background: var(--page); overflow: hidden;
    box-shadow: 4px 6px 10px rgba(0,0,0,0.45);
  }
  .page--front { left: 76px; }
  .page--back { left: 638px; }
  .page__photos { position: absolute; left: 0; top: 0; width: 486px; height: 628px; }

  .brand {
    position: absolute; top: 30px; left: 145px; width: 200px; text-align: center;
  }
  .brand__name {
    font-family: "Cinzel", Georgia, serif; font-weight: 400;
    font-size: 15px; letter-spacing: 3px; color: var(--white);
  }
  .brand__role {
    margin-top: 4px; font-size: 6px; letter-spacing: 2px; color: var(--grey-text);
  }

  .welcome {
    position: absolute; left: 28px; top: 416px;
    font-family: "Cinzel", Georgia, serif; font-weight: 700;
    font-size: 20px; line-height: 23px; color: var(--gold);
  }

  .bullets { position: absolute; list-style: none; font-size: 8.4px; line-height: 10.5px; }
  .bullets li { position: relative; padding-left: 0; }
  .bullets li::before {
    content: ""; position: absolute; left: -18px; top: 2px;
    width: 5px; height: 5px; background: var(--white); transform: rotate(45deg);
  }
  .bullets--front { left: 48px; top: 494px; width: 420px; }
  .bullets--front li { margin-bottom: 10.5px; }

  .section-title {
    position: absolute; left: 36px;
    font-family: "Cinzel", Georgia, serif; font-weight: 700;
    font-size: 20px; color: var(--gold);
  }
  .section-rule { position: absolute; left: 32px; width: 198px; height: 1px; background: var(--gold); }

  .how-title { top: 205px; }
  .how-rule { top: 230px; }
  .how-list { left: 54px; top: 239px; width: 390px; }
  .how-list li { margin-bottom: 10.5px; }

  .incl-title { top: 289px; }
  .incl-rule { top: 314px; }
  .incl-list { left: 58px; top: 324px; width: 370px; }
  .incl-list li { margin-bottom: 10.4px; }

  .invest-title { top: 438px; }
  .invest-rule { top: 463px; }
  .invest-list { left: 58px; top: 474px; width: 370px; }
  .invest-list li { margin-bottom: 10.5px; }

  .camera { position: absolute; left: 310px; top: 370px; width: 148px; height: 83px; }

  .summary {
    position: absolute; left: 18px; top: 551px; width: 451px; height: 63px;
    background: var(--summary-bg);
  }
  .summary__ribbon { position: absolute; left: 154px; top: 538px; width: 180px; height: 27px; }
  .summary__title {
    position: absolute; left: 154px; top: 540px; width: 180px; text-align: center;
    font-family: "Cinzel", Georgia, serif; font-weight: 700; font-size: 19px; color: #111;
  }
  .summary__text {
    position: absolute; left: 18px; top: 577px; width: 451px; padding: 0 26px;
    text-align: center; font-size: 8.2px; line-height: 10.6px; color: var(--summary-text);
  }
</style>
</head>
<body>

<section class="page page--front">
  <svg class="page__photos" viewBox="0 0 486 628" aria-hidden="false">
    <defs>
      <linearGradient id="front-hall" x1="0" y1="0" x2="1" y2="1">
        <stop offset="0" stop-color="#d8d2c6"/><stop offset="1" stop-color="#6b4a2c"/>
      </linearGradient>
      <linearGradient id="front-coast" x1="0" y1="0" x2="0" y2="1">
        <stop offset="0" stop-color="#c9b8c8"/><stop offset="0.6" stop-color="#6e8aa6"/><stop offset="1" stop-color="#3a4a3a"/>
      </linearGradient>
      <linearGradient id="front-lounge" x1="0" y1="0" x2="0" y2="1">
        <stop offset="0" stop-color="#8a5d3a"/><stop offset="0.5" stop-color="#2f4d78"/><stop offset="1" stop-color="#6f6a62"/>
      </linearGradient>
      <linearGradient id="front-kitchen" x1="0" y1="0" x2="0" y2="1">
        <stop offset="0" stop-color="#f2efe9"/><stop offset="0.6" stop-color="#c9ad8a"/><stop offset="1" stop-color="#8f8a84"/>
      </linearGradient>
      <linearGradient id="front-house" x1="0" y1="0" x2="0" y2="1">
        <stop offset="0" stop-color="#a9a2c4"/><stop offset="0.5" stop-color="#d9d6d2"/><stop offset="1" stop-color="#8c8578"/>
      </linearGradient>
    </defs>
    <polygon points="0,0 116,0 256,250 0,250" fill="url(#front-hall)" role="img" aria-label="Hallway with framed pictures, wooden bench and woven basket"/>
    <polygon points="380,0 486,0 486,78 324,78" fill="url(#front-coast)" role="img" aria-label="Dark clad house on a coastal cliff at dusk"/>
    <polygon points="196,96 486,96 486,278 288,278" fill="url(#front-lounge)" role="img" aria-label="Timber ceilinged living room with tall windows and a hanging fireplace"/>
    <polygon points="0,268 200,268 276,404 0,404" fill="url(#front-kitchen)" role="img" aria-label="Bright kitchen and dining table with white chairs"/>
    <polygon points="240,298 486,298 486,452 324,452" fill="url(#front-house)" role="img" aria-label="White farmhouse exterior with stone chimney at twilight"/>
  </svg>

  <div class="brand">
    <div class="brand__name">KEL DARROW</div>
    <div class="brand__role">PHOTOGRAPHER</div>
  </div>

  <h1 class="welcome">Welcome to the KLD<br>Real Estate Photography<br>Editing and Support Service</h1>

  <ul class="bullets bullets--front">
    <li>Take your real estate business to the next level by providing impressive real estate imagery that makes you stands out from the competition</li>
    <li>Omit the stress of trying to find a good photographer or managing an unreliable one and hence have more time to focus on other aspects of your business</li>
    <li>Showcase your listings with better quality and more impactful photographs than your competitors thereby increasing potential for a quick sale</li>
    <li>Great first impressions matter and you will achieve this by looking and feeling more professional. This will attract and retain more future clients.</li>
  </ul>
</section>

<section class="page page--back">
  <svg class="page__photos" viewBox="0 0 486 628">
    <defs>
      <linearGradient id="back-sofa" x1="0" y1="0" x2="1" y2="1">
        <stop offset="0" stop-color="#9fa3a6"/><stop offset="0.6" stop-color="#3c3f44"/><stop offset="1" stop-color="#b8b3aa"/>
      </linearGradient>
      <linearGradient id="back-lounge" x1="0" y1="0" x2="0" y2="1">
        <stop offset="0" stop-color="#7a5234"/><stop offset="0.5" stop-color="#3d6a96"/><stop offset="1" stop-color="#a88a68"/>
      </linearGradient>
      <linearGradient id="back-bedroom" x1="0" y1="0" x2="1" y2="0">
        <stop offset="0" stop-color="#c9c3b8"/><stop offset="0.5" stop-color="#9aa68a"/><stop offset="1" stop-color="#f1efec"/>
      </linearGradient>
    </defs>
    <polygon points="0,0 118,0 218,182 0,182" fill="url(#back-sofa)" role="img" aria-label="Grey sofa with cushions and a brass side table in window light"/>
    <polygon points="374,0 486,0 486,78 326,78" fill="url(#back-lounge)" role="img" aria-label="Open plan living room with glass walls and a hanging fireplace"/>
    <polygon points="194,97 486,97 486,221 290,221" fill="url(#back-bedroom)" role="img" aria-label="White bedroom with large windows overlooking green hills"/>
  </svg>

  <div class="brand">
    <div class="brand__name">KEL DARROW</div>
    <div class="brand__role">PHOTOGRAPHER</div>
  </div>

  <h2 class="section-title how-title">HOW IT WORKS</h2>
  <div class="section-rule how-rule"></div>
  <ul class="bullets how-list">
    <li>We understand that your time is valuable, so let us handle the editing and delivery of your images. You shoot, and we take care of the rest.</li>
    <li>Images are edited and delivered within 1 working day</li>
  </ul>

  <h2 class="section-title incl-title">INCLUSIONS:</h2>
  <div class="section-rule incl-rule"></div>
  <ul class="bullets incl-list">
    <li>Full day face to face training (we come to you) and instructional handbook</li>
    <li>We will teach you everything you need to know about your equipment and how to take stunning real estate photographs</li>
    <li>Service turnaround within 1 working day</li>
    <li>Free HELP desk service Mon-Fri</li>
    <li>12 month Exclusivity (rural towns only) for a limited time</li>
  </ul>

  <svg class="camera" viewBox="0 0 148 83">
    <defs>
      <linearGradient id="camera-body" x1="0" y1="0" x2="1" y2="1">
        <stop offset="0" stop-color="#3a3a3c"/><stop offset="1" stop-color="#121214"/>
      </linearGradient>
    </defs>
    <rect x="0" y="0" width="148" height="83" rx="10" fill="url(#camera-body)" role="img" aria-label="Mirrorless camera with lens and flip-out screen"/>
  </svg>

  <h2 class="section-title invest-title">INVESTMENT</h2>
  <div class="section-rule invest-rule"></div>
  <ul class="bullets invest-list">
    <li>99 per listing for us to manage images including editing, quality control and delivery (10 Images)</li>
    <li>Ask us about competitive packages for photography equipment if required</li>
  </ul>

  <div class="summary"></div>
  <svg class="summary__ribbon" viewBox="0 0 180 27">
    <polygon points="10,0 170,0 180,13 170,27 10,27 0,13" fill="var(--gold)"/>
  </svg>
  <h2 class="summary__title">SUMMARY</h2>
  <p class="summary__text">The KLD Real Estate Photography Editing and Support Service is the perfect solution for busy real estate professionals who want to take their business to the next level. Our service is affordable, flexible, and designed to help you showcase your listings in the best possible light.</p>
</section>

</body>
</html>
```